Labels for probiotic care products as Body Cream, Shower gel, Hand soap, ....

We are a starting a business in Flanders Belgium. We are looking for a label for care products, based on probiotics or good bacterie. We are looking for a fresh design that attracts people who wants a good product, based on naturally components. The products make that the microflora of the skin becomes and remains natural. The label must we be adaptive on bottles of 15 cm height to 8 cm height and a width of 4,5 cm. The brand name is KOVA REMU (beautiful skin in Hawaiian) or maybe just KOVA.

Industry/Entity Type

Business

Colors

Designer to choose colors to be used in the design.

Requirements
Must have
• somewhere the text "Probiotic Skin Care"
• I also have to tell that the bottles are white.
Nice to have
• I uploaded the 9 existing labels, but I want a totally new one, because the labels of our cleaning products are the same. I also uploaded a mood bord of labels I like.

```html
<!DOCTYPE html>
<html lang="nl">
<head>
<meta charset="utf-8">
<title>KOVA REMU – Skin Repair label</title>
<link rel="stylesheet" href="https://fonts.googleapis.com/css2?family=Jost:wght@400;500&family=Oswald:wght@300&display=swap">
<style>
  :root {
    --stage: #b4b4b4;
    --label-light: #f6f6f6;
    --label-mid: #e9e9e9;
    --ink-grey: #6f6f6f;
    --ink-dark: #2b2b2b;
    --leaf: #9dbb1f;
    --band-light: #cfcfcf;
    --band-dark: #a5a5a5;
    --rule: #8a8a8a;
  }
  * { margin: 0; padding: 0; box-sizing: border-box; }
  html, body { width: 900px; height: 1200px; overflow: hidden; }
  body {
    background: var(--stage);
    position: relative;
    font-family: "Jost", sans-serif;
  }
  .label {
    position: absolute;
    left: 178px;
    top: 50px;
    width: 544px;
    height: 1100px;
    background: linear-gradient(90deg, var(--label-mid) 0%, var(--label-light) 35%, var(--label-light) 70%, var(--label-mid) 100%);
    overflow: hidden;
  }
  .pattern-area {
    position: absolute;
    left: 0;
    width: 100%;
  }
  .pattern-area--top {
    top: 0;
    height: 135px;
    background: linear-gradient(180deg, #e4e4e4 0%, rgba(240,240,240,0) 100%);
  }
  .pattern-area--bottom {
    top: 770px;
    height: 136px;
    background: linear-gradient(0deg, #e2e2e2 0%, rgba(240,240,240,0) 100%);
  }
  .brand {
    position: absolute;
    left: 16px;
    top: 214px;
    display: flex;
    align-items: center;
    gap: 14px;
  }
  .brand__dot {
    width: 20px;
    height: 20px;
    background: var(--leaf);
  }
  .brand__name {
    font-family: "Jost", sans-serif;
    font-weight: 500;
    font-size: 38px;
    letter-spacing: 2px;
    color: var(--ink-dark);
    line-height: 1;
  }
  .product-title {
    position: absolute;
    left: 0;
    top: 0;
    width: 544px;
    height: 906px;
  }
  .product-title text {
    font-family: "Jost", sans-serif;
    font-weight: 400;
    font-size: 150px;
    fill: var(--leaf);
  }
  .tagline {
    position: absolute;
    left: 13px;
    top: 763px;
    width: 280px;
    height: 61px;
    border-top: 2px solid var(--rule);
    border-bottom: 2px solid var(--rule);
    display: flex;
    align-items: center;
    padding-left: 2px;
  }
  .tagline__text {
    font-family: "Jost", sans-serif;
    font-size: 31px;
    color: var(--ink-grey);
    white-space: nowrap;
  }
  .info-band {
    position: absolute;
    left: 0;
    top: 906px;
    width: 100%;
    height: 184px;
    background: linear-gradient(180deg, var(--band-light) 0%, #bdbdbd 60%, var(--band-dark) 100%);
    padding: 26px 14px 0;
  }
  .info-band__slogan {
    font-family: "Jost", sans-serif;
    font-size: 34px;
    color: #3a3a3a;
    letter-spacing: 0.5px;
    line-height: 1;
  }
  .info-band__slogan strong { font-weight: 500; color: var(--ink-dark); }
  .info-band__copy {
    margin-top: 18px;
    font-family: "Oswald", sans-serif;
    font-weight: 300;
    font-size: 20px;
    line-height: 30px;
    color: var(--ink-dark);
    width: 440px;
  }
  .leaf-rule {
    position: absolute;
    left: 0;
    top: 1090px;
    width: 100%;
    height: 5px;
    background: var(--leaf);
  }
</style>
</head>
<body>
  <main class="label">
    <div class="pattern-area pattern-area--top" role="img" aria-label="Faint grey geometric line pattern"></div>
    <div class="pattern-area pattern-area--bottom" role="img" aria-label="Faint grey geometric line pattern"></div>

    <svg class="product-title" viewBox="0 0 544 906" aria-label="Skin Repair">
      <text transform="translate(310 60) rotate(90)" textLength="700" lengthAdjust="spacingAndGlyphs">Skin Repair</text>
    </svg>

    <div class="brand">
      <span class="brand__dot"></span>
      <span class="brand__name">KOVA REMU</span>
    </div>

    <div class="tagline">
      <span class="tagline__text">Probiotic Skin Care</span>
    </div>

    <section class="info-band">
      <p class="info-band__slogan">BEAUTIFUL BY <strong>NATURE</strong></p>
      <p class="info-band__copy">Een probiotische huidcrème, voor volwassenen en kinderen. Dagelijks gebruik vormt een beschermende goede huidflora en reinigt diep. Aanbrengen op een droge huid.</p>
    </section>

    <div class="leaf-rule"></div>
  </main>
</body>
</html>
```